Header-Banner für Newsletter-/Journey-Mails
Zielgruppe
Wir, der Morvik Verlag sind der führende Verlag für Kinderbücher und Comics.
Aufgabenstellung
Wir suchen übergangsweise - bis zum Relaunch unserer Website - einen Header-Banner für unserer Newsletter/Journey-Mails.
Das Morvik Comics Logo sollte enthalten sein. Das Design des Banner sollte eine moderne, nicht verspielte, anspruchsvolle, grafisch orientierte Zielgruppe ansprechen.
Bitte keine Fotos und nicht selbst illustrieren.
Maße: Breite 600 px - Höhe max. 300 Pixel.

```html
<!DOCTYPE html>
<html lang="en">
<head>
<meta charset="utf-8">
<title>Morvik Comics – Newsletter Header</title>
<link rel="stylesheet" href="https://fonts.googleapis.com/css2?family=Open+Sans:wght@400;600;700&display=swap">
<style>
  :root {
    --green-deep: #2a8a3c;
    --green-mid: #3e9e44;
    --green-light: #6dc04c;
    --green-blob: #4aa84a;
    --text-white: #ffffff;
    --text-soft: #b9e0a6;
    --icon-soft: #d9efcf;
    --brand-orange: #f7931e;
  }
  * { margin: 0; padding: 0; box-sizing: border-box; }
  html, body { width: 1200px; height: 600px; overflow: hidden; }
  body { font-family: "Open Sans", sans-serif; }

  .banner {
    position: relative;
    width: 1200px;
    height: 600px;
    overflow: hidden;
    background: linear-gradient(120deg, var(--green-deep) 0%, var(--green-mid) 45%, var(--green-light) 100%);
  }
  .banner__wave {
    position: absolute;
    inset: 0;
  }

  .brand {
    position: absolute;
    left: 58px;
    top: 64px;
    display: flex;
    align-items: center;
    gap: 14px;
  }
  .brand__mark {
    width: 34px;
    height: 34px;
    background: var(--brand-orange);
  }
  .brand__name {
    font-size: 34px;
    font-weight: 700;
    color: var(--text-white);
    letter-spacing: 0.5px;
  }

  .headline {
    position: absolute;
    left: 110px;
    top: 246px;
    color: var(--text-white);
    font-weight: 600;
    line-height: 1.08;
  }
  .headline__lead { display: block; font-size: 40px; }
  .headline__main { display: block; font-size: 54px; }

  .intro {
    position: absolute;
    left: 110px;
    top: 368px;
    width: 470px;
    font-size: 16.5px;
    line-height: 26px;
    color: var(--text-soft);
  }

  .social {
    position: absolute;
    left: 56px;
    top: 536px;
    display: flex;
    gap: 38px;
    list-style: none;
    align-items: center;
  }
  .social__item { width: 24px; height: 24px; }
  .social__dot {
    display: block;
    width: 22px;
    height: 22px;
    border-radius: 50%;
    border: 3px solid var(--icon-soft);
  }

  .illustration {
    position: absolute;
    left: 590px;
    top: 80px;
    width: 530px;
    height: 460px;
    border-radius: 48% 52% 40% 60% / 46% 38% 62% 54%;
    background: radial-gradient(circle at 55% 60%, #2f8f3a 0%, #3a9a44 55%, rgba(74,168,74,0.3) 100%);
  }
</style>
</head>
<body>
  <main class="banner">
    <svg class="banner__wave" width="1200" height="600" viewBox="0 0 1200 600" aria-hidden="true">
      <path d="M0 0 H620 C560 120 420 150 300 120 C180 90 80 60 0 90 Z" fill="#ffffff" opacity="0.05"/>
      <path d="M0 470 C160 430 320 470 420 540 C470 575 500 600 520 600 H0 Z" fill="#ffffff" opacity="0.05"/>
      <path d="M760 0 C900 60 1080 40 1200 0 V300 C1120 200 980 160 860 120 Z" fill="#ffffff" opacity="0.06"/>
    </svg>

    <div class="brand">
      <span class="brand__mark"></span>
      <span class="brand__name">Morvik Comics</span>
    </div>

    <h1 class="headline">
      <span class="headline__lead">Subscribe to our</span>
      <span class="headline__main">Newsletter!</span>
    </h1>

    <p class="intro">Lorem ipsum dolor sit amet, consectetur adipiscing elit, nec sit amet felis. Aenean pharetra urna urna, tetur velit aliquam quis.</p>

    <ul class="social" aria-label="Share and follow">
      <li class="social__item">
        <svg width="24" height="24" viewBox="0 0 24 24" aria-label="Share">
          <g fill="var(--icon-soft)" stroke="var(--icon-soft)" stroke-width="2">
            <line x1="6" y1="12" x2="18" y2="5"/>
            <line x1="6" y1="12" x2="18" y2="19"/>
            <circle cx="5" cy="12" r="3.2" stroke="none"/>
            <circle cx="19" cy="4.5" r="3.2" stroke="none"/>
            <circle cx="19" cy="19.5" r="3.2" stroke="none"/>
          </g>
        </svg>
      </li>
      <li class="social__item"><span class="social__dot" aria-label="Social network"></span></li>
      <li class="social__item"><span class="social__dot" aria-label="Social network"></span></li>
      <li class="social__item"><span class="social__dot" aria-label="Social network"></span></li>
    </ul>

    <div class="illustration" role="img" aria-label="Illustration of a child lying on the floor reading a comic book, with a sleeping dog, a potted plant, a stack of books and a bookshelf"></div>
  </main>
</body>
</html>
```